buseisness card

design a card that similar to my web site
TRELLINGWORKSLLC .COM

Contact Information for Business Card

NAME PHONE # WEBSITE EMAIL AND DISCTIPTION OF WHAT WE DO

Colors
0054AA
0677BA
7BADD7
CADEEF
E8F1F8

Requirements
Must have
• lOGO AND DETAILS
Nice to have
• I LIKE THE WATER LIKE ON MY WEB SITE

```html
<!DOCTYPE html>
<html lang="en">
<head>
<meta charset="utf-8">
<title>Trelling Works – Business Card</title>
<link rel="stylesheet" href="https://fonts.googleapis.com/css2?family=Montserrat:wght@700&family=Open+Sans:wght@400;700&display=swap">
<style>
  :root{
    --deep-blue:#0d3a7a;
    --bright-blue:#0a7cc1;
    --brand-blue:#2381b6;
    --accent-blue:#1565c0;
    --water-light:#7badd7;
    --rule:#d4e6f2;
    --ghost:#eef3f9;
    --stage:#ebebee;
    --white:#ffffff;
  }
  *{margin:0;padding:0;box-sizing:border-box}
  html,body{width:1200px;height:1200px;overflow:hidden;background:var(--stage)}
  .card{position:absolute;left:172px;width:873px;height:499px;overflow:hidden}

  /* Front */
  .card--front{top:57px;background:linear-gradient(90deg,var(--deep-blue) 0%,#17569a 50%,var(--bright-blue) 100%)}
  .water-area{position:absolute;left:505px;top:0;width:368px;height:499px;
    background:radial-gradient(ellipse at 55% 45%,rgba(123,173,215,.35),rgba(123,173,215,0) 70%)}
  .front-mark{position:absolute;left:40px;top:90px;display:flex;align-items:center;gap:18px}
  .front-mark__dot{width:120px;height:120px;border-radius:50%;background:var(--brand-blue)}
  .front-mark__name{font:700 26px "Montserrat",sans-serif;color:var(--brand-blue);letter-spacing:1px}
  .front-title{position:absolute;right:32px;top:412px;font:700 50px/1 "Montserrat",sans-serif;
    color:var(--white);letter-spacing:2px;white-space:nowrap}

  /* Back */
  .card--back{top:620px;background:var(--white);border:1px solid #d8d8dc}
  .ghost-dot{position:absolute;left:585px;top:60px;width:430px;height:430px;border-radius:50%;background:var(--ghost)}
  .back-mark{position:absolute;left:170px;top:40px;display:flex;align-items:center;gap:14px}
  .back-mark__dot{width:110px;height:110px;border-radius:50%;background:var(--brand-blue)}
  .back-mark__name{font:700 18px "Montserrat",sans-serif;color:var(--brand-blue);letter-spacing:1px}
  .company{position:absolute;left:24px;top:226px;font:700 52px/1 "Montserrat",sans-serif;
    color:var(--brand-blue);letter-spacing:2px;white-space:nowrap}
  .person{position:absolute;right:34px;top:298px;text-align:right;font-family:"Open Sans",sans-serif;color:var(--brand-blue)}
  .person__name{font-weight:700;font-size:25px;letter-spacing:3px;line-height:1}
  .person__role{font-size:21px;letter-spacing:1px;line-height:1.3;margin-top:4px}
  .accent-bar{position:absolute;right:0;top:316px;width:12px;height:42px;background:var(--accent-blue)}
  .divider{position:absolute;left:24px;top:366px;width:820px;height:1px;background:var(--rule)}
  .address{position:absolute;left:24px;top:384px;font:400 24px/29px "Open Sans",sans-serif;color:var(--brand-blue)}
  .contacts{position:absolute;right:26px;top:384px;list-style:none;font:400 24px/29px "Open Sans",sans-serif;color:var(--brand-blue);text-align:right}
  .contacts li{display:flex;align-items:center;justify-content:flex-end;gap:12px;height:29px}
  .contacts svg{width:18px;height:18px;fill:var(--brand-blue)}
  .bottom-band{position:absolute;left:0;bottom:0;width:100%;height:8px;background:linear-gradient(90deg,var(--accent-blue),var(--bright-blue))}
</style>
</head>
<body>
  <section class="card card--front">
    <div class="water-area" role="img" aria-label="Water droplets and bubbles scattered over the blue background"></div>
    <div class="front-mark">
      <span class="front-mark__dot"></span>
      <span class="front-mark__name">TRELLING WORKS</span>
    </div>
    <h1 class="front-title">TRELLING WORKS</h1>
  </section>

  <section class="card card--back">
    <span class="ghost-dot"></span>
    <div class="back-mark">
      <span class="back-mark__dot"></span>
      <span class="back-mark__name">TRELLING WORKS</span>
    </div>
    <h2 class="company">TRELLING WORKS</h2>
    <div class="person">
      <p class="person__name">MARCUS HALE</p>
      <p class="person__role">Manager</p>
    </div>
    <span class="accent-bar"></span>
    <span class="divider"></span>
    <address class="address" style="font-style:normal">
      1480 Riverside Commons<br>Dayton<br>OH 45402
    </address>
    <ul class="contacts">
      <li>+740 555 0187
        <svg viewBox="0 0 24 24"><path d="M6.6 10.8a15 15 0 0 0 6.6 6.6l2.2-2.2c.3-.3.7-.4 1-.2 1.1.4 2.3.6 3.6.6.6 0 1 .4 1 1V20c0 .6-.4 1-1 1A17 17 0 0 1 3 4c0-.6.4-1 1-1h3.5c.6 0 1 .4 1 1 0 1.3.2 2.5.6 3.6.1.3 0 .7-.2 1z"/></svg>
      </li>
      <li>mh@tw208.com
        <svg viewBox="0 0 24 24"><path d="M2 5h20v2l-10 6L2 7zm0 4 10 6 10-6v10H2z"/></svg>
      </li>
      <li>www.trellingworksllc.com
        <svg viewBox="0 0 24 24" fill="none" stroke="#2381b6" stroke-width="1.6" style="fill:none"><circle cx="12" cy="12" r="9.5"/><ellipse cx="12" cy="12" rx="4.2" ry="9.5"/><path d="M2.5 12h19M4 7h16M4 17h16"/></svg>
      </li>
    </ul>
    <span class="bottom-band"></span>
  </section>
</body>
</html>
```